Tending Our Garden eBook Cover Design

I want to deisgn a cover for my eBook (FRONT COVER) and the title is:

UNDER THE WILLOW TREE; WHERE I FOUND MY QUIET STRENGTH AND WHERE YOU MIGHT TOO
By KT Dorran

TITLE CHANGED TO: UNDER THE WILLOW TREE; WHERE I FOUND MY QUIET STRENGTH AND WHERE YOU MIGHT TOO

The color palette is attached. Along with some photos options of me. Along with the ebook in WORD Document. My website is www.KTDorranLive.example. You can use a different color palette if you think it is best

Target Market(s)

women who look to build a personal brand

Industry/Entity Type

health and wellness

Requirements
Must have
• the title
Nice to have
• use my picture on the cover; but that is optional
Should not have
• any men

```html
<!DOCTYPE html>
<html lang="en">
<head>
<meta charset="utf-8">
<title>Under the Willow Tree — KT Dorran</title>
<link href="https://fonts.googleapis.com/css2?family=Bebas+Neue&display=swap" rel="stylesheet">
<style>
  :root {
    --backdrop: #d3d5d7;
    --cover-blush: #e0bba6;
    --cover-brown: #553426;
    --cover-white: #ffffff;
    --photo-warm: #d49f80;
    --photo-gold: #dfb48c;
  }
  html, body {
    margin: 0;
    width: 1117px;
    height: 1200px;
    overflow: hidden;
    background: var(--backdrop);
  }
  .cover {
    position: absolute;
    left: 188px;
    top: 43px;
    width: 740px;
    height: 1114px;
    display: block;
  }
  .title-text {
    font-family: "Bebas Neue", "Oswald", sans-serif;
    fill: var(--cover-brown);
  }
  .title-text.light { fill: var(--cover-white); }
  .author-name {
    font-family: "Bebas Neue", "Oswald", sans-serif;
    fill: var(--cover-white);
    letter-spacing: 1px;
  }
</style>
</head>
<body>
<svg class="cover" viewBox="0 0 740 1114" xmlns="http://www.w3.org/2000/svg">
  <defs>
    <linearGradient id="photo-fade" x1="0" y1="0" x2="0" y2="1">
      <stop offset="0" stop-color="var(--cover-blush)" stop-opacity="1"/>
      <stop offset="0.25" stop-color="var(--photo-warm)" stop-opacity="0.7"/>
      <stop offset="0.7" stop-color="var(--photo-gold)" stop-opacity="0.9"/>
      <stop offset="1" stop-color="var(--photo-warm)" stop-opacity="1"/>
    </linearGradient>
  </defs>

  <rect class="cover-ground" x="0" y="0" width="740" height="1114" fill="var(--cover-blush)"/>

  <g class="cover-photo" role="img" aria-label="Warm-toned photo of stacked gold coins in front of a soft financial chart">
    <rect x="0" y="550" width="740" height="480" fill="url(#photo-fade)"/>
  </g>

  <!-- title -->
  <text class="title-text" x="47" y="118" font-size="96" textLength="647" lengthAdjust="spacingAndGlyphs">UNDER THE WILLOW TREE;</text>

  <g class="title-divider">
    <path d="M47 160 L278 158 L278 162 Z" fill="var(--cover-brown)"/>
    <path d="M694 160 L462 158 L462 162 Z" fill="var(--cover-brown)"/>
    <text class="title-text" x="370" y="171" font-size="31" text-anchor="middle">WHERE I FOUND</text>
  </g>

  <text class="title-text" x="47" y="337" font-size="210" textLength="647" lengthAdjust="spacingAndGlyphs">MY QUIET</text>
  <text class="title-text" x="47" y="526" font-size="230" textLength="647" lengthAdjust="spacingAndGlyphs">STRENGTH</text>

  <g class="title-divider light">
    <path d="M47 570 L332 568.5 L332 571.5 Z" fill="var(--cover-white)"/>
    <path d="M694 570 L408 568.5 L408 571.5 Z" fill="var(--cover-white)"/>
    <text class="title-text light" x="370" y="582" font-size="34" text-anchor="middle">AND</text>
  </g>

  <text class="title-text light" x="47" y="690" font-size="100" textLength="647" lengthAdjust="spacingAndGlyphs">WHERE YOU MIGHT TOO</text>

  <!-- torn paper edge and author band -->
  <path class="torn-edge" fill="var(--cover-white)"
        d="M0 1010 L20 1006 L38 1012 L55 1004 L74 1009 L92 1001 L110 1008 L130 1003 L150 1010 L168 1002 L186 1007 L205 999 L224 1006 L244 1001 L262 1008 L282 1000 L300 1006 L320 998 L340 1005 L360 1000 L380 1007 L400 999 L420 1005 L440 998 L458 1004 L478 999 L498 1006 L518 1000 L538 1007 L558 1001 L578 1006 L598 999 L618 1005 L640 1000 L660 1008 L680 1002 L700 1009 L720 1004 L740 1010 L740 1040 L0 1040 Z"/>
  <path class="author-band" fill="var(--cover-brown)"
        d="M0 1028 L22 1022 L44 1030 L66 1021 L88 1027 L112 1019 L136 1026 L160 1020 L184 1027 L208 1018 L232 1025 L256 1019 L280 1026 L304 1017 L328 1024 L352 1018 L376 1025 L400 1017 L424 1024 L448 1019 L472 1026 L496 1018 L520 1025 L544 1020 L568 1027 L592 1019 L616 1026 L640 1021 L664 1028 L688 1022 L712 1030 L740 1024 L740 1114 L0 1114 Z"/>
  <text class="author-name" x="370" y="1086" font-size="40" text-anchor="middle">BY KT DORRAN</text>
</svg>
</body>
</html>
```